Brightfold Systems, a software development company, needs a website

We need a website to promote our software development company. The company is brand new and we want to market ourselves. We develop all kinds of software from web applications, to desktop applications, to mobile applications. Small company, not a lot of history, just need something flashy.

```html
<!DOCTYPE html>
<html lang="en">
<head>
<meta charset="utf-8">
<title>Brightfold Systems — Software Development</title>
<link rel="stylesheet" href="https://fonts.googleapis.com/css2?family=Montserrat:ital,wght@0,400;0,500;0,600;0,700;1,400&display=swap">
<style>
:root{
  --blue:#2f5fe0;
  --navy:#1d2a4d;
  --ink:#1f2330;
  --muted:#6e7486;
  --pale:#f3f6fc;
  --line:#e3e6ee;
  --white:#ffffff;
  --star:#e6b323;
}
*{box-sizing:border-box;margin:0;padding:0}
html,body{width:1200px;height:3515px;overflow:hidden}
body{position:relative;font-family:"Montserrat",sans-serif;color:var(--ink);background:var(--white)}
.abs{position:absolute}
.center{left:0;width:1200px;text-align:center}
.eyebrow{font-size:11px;font-weight:600;letter-spacing:1px;color:var(--blue);text-transform:uppercase}
.section-title{font-size:32px;font-weight:500;color:var(--ink)}
.read-more{font-size:13px;font-style:italic;color:var(--blue);text-decoration:none}

/* hero */
.hero{left:0;top:0;width:1200px;height:591px;background:linear-gradient(180deg,#3a4f7a 0%,#2c3c5e 55%,#1f2b44 100%)}
.hero-shade{left:0;top:0;width:1200px;height:591px;background:linear-gradient(90deg,rgba(40,60,100,.35),rgba(20,30,55,.15))}
.topbar-line{left:0;top:66px;width:1200px;height:1px;background:rgba(255,255,255,.2)}
.brand{display:flex;align-items:center;gap:8px;font-weight:600;font-size:19px}
.brand-dot{width:12px;height:12px;border-radius:50%}
.nav{top:29px;left:632px;display:flex;gap:32px;font-size:13px;color:var(--white)}
.signin{left:941px;top:20px;width:97px;height:35px;border:2px solid var(--white);border-radius:18px;color:var(--white);font-size:13px;display:flex;align-items:center;justify-content:center}
.hero-title{top:212px;font-size:50px;font-weight:700;line-height:61px;color:var(--white);letter-spacing:.5px}
.hero-sub{top:346px;font-size:15px;color:var(--white)}
.hero-btn{left:525px;top:400px;width:150px;height:35px;border-radius:18px;background:var(--blue);color:var(--white);font-size:10px;font-weight:600;letter-spacing:1px;display:flex;align-items:center;justify-content:center}

/* services */
.service{width:240px;text-align:center}
.service-icon{width:50px;height:50px;margin:0 auto;border-radius:6px;background:var(--white);box-shadow:0 4px 14px rgba(30,50,100,.1);display:flex;align-items:center;justify-content:center}
.service h3{margin-top:36px;font-size:14px;font-weight:600;color:var(--navy)}
.service p{margin-top:20px;font-size:11.5px;line-height:21px;color:var(--muted)}
.service .read-more{display:block;margin-top:12px}
.divider{left:163px;width:875px;height:1px;background:var(--line)}

/* project */
.blob{left:160px;top:1310px;width:385px;height:380px;background:var(--pale);border-radius:48% 52% 46% 54% / 40% 42% 58% 60%}
.phone{left:283px;top:1293px;width:197px;height:397px;border-radius:30px;background:#141414;padding:9px;box-shadow:18px 22px 30px rgba(20,30,60,.15)}
.phone-screen{position:relative;width:100%;height:100%;border-radius:22px;background:linear-gradient(160deg,#3a6bf0,#2a55d8)}
.phone-name{position:absolute;left:0;top:227px;width:100%;text-align:center;color:var(--white);font-size:17px;font-weight:600}
.project-title{left:613px;top:1368px;font-size:19px;font-weight:600;color:var(--blue)}
.project-text{left:613px;top:1407px;width:400px;font-size:12.5px;line-height:25.5px;color:var(--muted)}

/* clients */
.clients-band{left:0;top:1773px;width:1200px;height:562px;background:var(--pale)}
.review{width:277px;height:287px;padding:14px 28px}
.review.featured{background:var(--white);box-shadow:0 6px 24px rgba(30,50,100,.1)}
.reviewer{display:flex;align-items:center;gap:18px}
.avatar{width:38px;height:38px;border-radius:50%;background:linear-gradient(135deg,#d9a88a,#8d5b44)}
.reviewer b{display:block;font-size:13px;font-weight:600;color:var(--navy)}
.reviewer span{font-size:11px;color:#9aa0ae}
.review p{margin-top:22px;font-size:12px;line-height:23px;color:var(--muted)}
.stars{position:absolute;left:28px;top:248px;display:flex;gap:2px}

/* contact */
.contact-box{left:163px;top:2558px;width:875px;height:480px;background:var(--white);box-shadow:0 4px 24px rgba(30,50,100,.1)}
.map{left:168px;top:2563px;width:416px;height:470px;background:linear-gradient(135deg,#e4e4e4,#d2d2d2)}
.map-card{left:275px;top:2737px;width:206px;height:106px;background:var(--white);border-radius:4px;box-shadow:0 3px 10px rgba(0,0,0,.15);padding:16px 10px;font-size:11px;line-height:16px;color:var(--ink)}
.map-card div{display:flex;gap:6px;align-items:flex-start}
.field{left:652px;width:316px;height:38px;border:1px solid var(--line);border-radius:19px;padding:11px 17px;font-size:11px;color:#9aa0ae}
.field.message{border-radius:6px;height:115px}
.submit{left:652px;top:2936px;width:316px;height:38px;border-radius:19px;background:var(--blue);color:var(--white);font-size:13px;font-weight:600;display:flex;align-items:center;justify-content:center;box-shadow:0 8px 18px rgba(47,95,224,.3)}

/* footer */
.footer-band{left:0;top:3130px;width:1200px;height:385px;background:var(--pale)}
.footer-about{left:163px;top:3288px;width:230px;font-size:11.5px;line-height:20px;color:var(--muted)}
.footer-col h4{font-size:16px;font-weight:600;letter-spacing:.5px;color:var(--navy)}
.footer-col ul{list-style:none;margin-top:20px}
.footer-col li{font-size:11.5px;color:var(--muted);height:27.5px;display:flex;align-items:center;gap:12px}
.social-dot{width:12px;height:12px;border-radius:50%;background:var(--blue)}
.footer-rule{left:163px;top:3470px;width:875px;height:1px;background:var(--line)}
.copyright{top:3490px;font-size:10.5px;color:var(--muted)}
</style>
</head>
<body>

<!-- hero -->
<div class="abs hero" role="img" aria-label="Photo of developers working at computers in an office"></div>
<div class="abs hero-shade"></div>
<div class="abs topbar-line"></div>
<div class="abs brand" style="left:163px;top:22px;color:var(--white)"><span class="brand-dot" style="border:2px solid var(--white)"></span>Brightfold Systems</div>
<nav class="abs nav"><span>Home</span><span>About</span><span>Services</span><span>Contact</span></nav>
<div class="abs signin">Sign in</div>
<h1 class="abs center hero-title">MOBILE APP, WEB,<br>API, IOT &amp; DEVELOPMENT</h1>
<p class="abs center hero-sub">Morbi accumsan ipsum velit. Nam nec tellus a odio tincidunt auctor a ornare odio.</p>
<div class="abs hero-btn">GET IN TOUCH</div>

<!-- services -->
<div class="abs center eyebrow" style="top:664px">What we do</div>
<h2 class="abs center section-title" style="top:695px">Services We Offer</h2>

<div class="abs service" style="left:180px;top:790px">
  <div class="service-icon"><svg width="28" height="28" viewBox="0 0 28 28" fill="none" stroke="#2bb3a3" stroke-width="1.5"><rect x="3" y="3" width="22" height="15" rx="1"/><path d="M11 8l-2 2.5 2 2.5M17 8l2 2.5-2 2.5M15 7.5l-2 6"/><path d="M10 22h8M14 18v4"/><circle cx="22" cy="23" r="2"/></svg></div>
  <h3>Web / API Developement</h3>
  <p>Aenean sollicitudin, lorem quis bibendum auctor, nisi elit consequat ipsum, nec sagittis sem.</p>
  <a class="read-more">Read More &gt;</a>
</div>
<div class="abs service" style="left:480px;top:790px">
  <div class="service-icon"><svg width="28" height="28" viewBox="0 0 28 28" fill="none" stroke="#e8506a" stroke-width="1.5"><rect x="7" y="2" width="13" height="24" rx="2"/><path d="M11 23h5"/><circle cx="17" cy="11" r="2.5"/><circle cx="12" cy="15" r="2"/><path d="M10 9h3"/></svg></div>
  <h3>Mobile App Developement</h3>
  <p>Aenean sollicitudin, lorem quis bibendum auctor, nisi elit consequat ipsum, nec sagittis sem.</p>
  <a class="read-more">Read More &gt;</a>
</div>
<div class="abs service" style="left:778px;top:790px">
  <div class="service-icon"><svg width="30" height="28" viewBox="0 0 30 28" fill="none" stroke="#2f5fe0" stroke-width="1.7" stroke-linecap="round"><path d="M3 10a17 17 0 0 1 24 0"/><path d="M7 14a11 11 0 0 1 16 0"/><path d="M11 18a5.5 5.5 0 0 1 8 0"/><circle cx="15" cy="22" r="1.6"/></svg></div>
  <h3>Internet of Things</h3>
  <p>Aenean sollicitudin, lorem quis bibendum auctor, nisi elit consequat ipsum, nec sagittis sem.</p>
  <a class="read-more">Read More &gt;</a>
</div>

<div class="abs divider" style="top:1092px"></div>

<!-- projects -->
<div class="abs center eyebrow" style="top:1147px">Our works</div>
<h2 class="abs center section-title" style="top:1170px">Latest Projects</h2>
<div class="abs blob"></div>
<div class="abs phone"><div class="phone-screen" role="img" aria-label="Mobile app splash screen on a blue photo background"><span class="phone-name">Brightfold Systems</span></div></div>
<h3 class="abs project-title">Mobile App Developement</h3>
<p class="abs project-text">Duis sed odio sit amet nibh vulputate cursus a sit amet mauris. Morbi accumsan ipsum velit. Nam nec tellus a odio tincidunt auctor a ornare odio. Sed non mauris vitae erat consequat auctor eu in elit. Class aptent taciti sociosqu ad litora torquent per conubia nostra, per inceptos himenaeos.</p>
<a class="abs read-more" style="left:613px;top:1553px">Read More &gt;</a>

<!-- clients -->
<div class="abs clients-band"></div>
<div class="abs center eyebrow" style="top:1848px">Our clients</div>
<h2 class="abs center section-title" style="top:1878px">What They Say</h2>

<div class="abs review" style="left:157px;top:1968px">
  <div class="reviewer"><div class="avatar" role="img" aria-label="Client portrait"></div><div><b>Maren, USA</b><span>Northmere University</span></div></div>
  <p>Duis sed odio sit amet nibh vulputate cursus a sit amet mauris. Morbi accumsan ipsum velit. Nam nec tellus a odio tincidunt auctor a ornare odio. Sed non mauris vitae erat consequat auctor eu in elit.</p>
  <div class="stars"><svg width="70" height="12" viewBox="0 0 70 12" fill="#e6b323"><g id="s"><path d="M6 0l1.8 3.9 4.2.4-3.2 2.8 1 4.1L6 9.1 2.2 11.2l1-4.1L0 4.3l4.2-.4z"/></g><use href="#s" x="14"/><use href="#s" x="28"/><use href="#s" x="42"/><use href="#s" x="56"/></svg></div>
</div>
<div class="abs review" style="left:459px;top:1968px">
  <div class="reviewer"><div class="avatar" role="img" aria-label="Client portrait"></div><div><b>Lidia, EU</b><span>Owner, Halden Works LLC</span></div></div>
  <p>Proin gravida nibh vel velit auctor aliquet. Aenean sollicitudin, lorem quis bibendum auctor, nisi elit consequat ipsum, nec sagittis sem nibh id elit.</p>
  <div class="stars"><svg width="70" height="12" viewBox="0 0 70 12" fill="#e6b323"><use href="#s"/><use href="#s" x="14"/><use href="#s" x="28"/><use href="#s" x="42"/><use href="#s" x="56"/></svg></div>
</div>
<div class="abs review featured" style="left:761px;top:1968px">
  <div class="reviewer"><div class="avatar" role="img" aria-label="Client portrait"></div><div><b>Teodora, NY</b><span>CEO, Pellwood</span></div></div>
  <p>Duis sed odio sit amet nibh vulputate cursus a sit amet mauris. Morbi accumsan ipsum velit. Nam nec tellus a odio tincidunt auctor a ornare odio. Sed non mauris vitae erat consequat auctor eu in elit.</p>
  <div class="stars"><svg width="70" height="12" viewBox="0 0 70 12" fill="#e6b323"><use href="#s"/><use href="#s" x="14"/><use href="#s" x="28"/><use href="#s" x="42"/><use href="#s" x="56"/></svg></div>
</div>

<!-- contact -->
<div class="abs center eyebrow" style="top:2390px">Contact us</div>
<h2 class="abs center section-title" style="top:2420px;line-height:50px">What are you waiting for ?<br>Let’s get on touch now</h2>
<div class="abs contact-box"></div>
<div class="abs map" role="img" aria-label="Grey street map of the office area"></div>
<div class="abs map-card">
  <div><svg width="12" height="14" viewBox="0 0 12 14" fill="#2f5fe0"><path d="M6 0a5 5 0 0 0-5 5c0 3.5 5 9 5 9s5-5.5 5-9a5 5 0 0 0-5-5zm0 7a2 2 0 1 1 0-4 2 2 0 0 1 0 4z"/></svg><span>14 Larkspur Lane, Eastvale</span></div>
  <div style="margin-top:24px"><svg width="12" height="12" viewBox="0 0 12 12" fill="#2f5fe0"><path d="M2.5 0L5 2.8 3.6 4.4a8 8 0 0 0 4 4L9.2 7 12 9.5 10.4 12C5 12 0 7 0 1.6z"/></svg><span>555-014-2288</span></div>
</div>
<div class="abs field" style="top:2615px">Name :</div>
<div class="abs field" style="top:2669px">Email :</div>
<div class="abs field" style="top:2723px">Phone :</div>
<div class="abs field message" style="top:2777px">Message :</div>
<div class="abs submit">SUBMIT</div>

<!-- footer -->
<div class="abs footer-band"></div>
<div class="abs brand" style="left:163px;top:3250px;color:var(--navy)"><span class="brand-dot" style="border:2px solid var(--blue)"></span>Brightfold Systems</div>
<p class="abs footer-about">Aenean sollicitudin, lorem quis bibendum auctor, nisi elit consequat ipsum, nec sagittis sem nibh id elit. Duis sed odio sit amet nibh vulputate cursus.</p>
<div class="abs footer-col" style="left:463px;top:3252px"><h4>SERVICES</h4><ul><li>Workshops</li><li>Internet of Things</li><li>Ux and Ui</li><li>Development</li><li>Implementation</li></ul></div>
<div class="abs footer-col" style="left:687px;top:3252px"><h4>QUICK LINKS</h4><ul><li>About</li><li>Services</li><li>Pricing</li><li>Blog</li><li>Contact</li></ul></div>
<div class="abs footer-col" style="left:915px;top:3252px"><h4>FOLLOW US</h4><ul><li><span class="social-dot"></span>Circlepost</li><li><span class="social-dot"></span>Chirpline</li><li><span class="social-dot"></span>Snapgrid</li><li><span class="social-dot"></span>Workreach</li></ul></div>
<div class="abs footer-rule"></div>
<div class="abs center copyright">© Copyright 2019 Brightfold Systems. All Rights Reserved</div>

</body>
</html>
```